Would like a Northwest feel to the look, something NOT typical of what you would see on a typical Home Inspectors logo. Real estate cards all the same as well, and would like to stand out. Earthy, green, Northwest. Sadly a portrait seems to be a requirement (see the attached). I inspect residential homes for buyers and sellers.

Target Market(s)

Home Buyers and Sellers

Industry/Entity Type

Home Inspection

Contact Information for Business Card

See description
Note: The name Corvaneth is a Chinook word that means 'Friend'. Please do not associate the name with the Whale that shows up on 99% of google searches.

Logo Text

Corvaneth Home Inspections

Colors

Designer to choose colors to be used in the design.

Requirements
Must have
• Phone Num: 541-672-8153
• Address: 732 SW 219th Av Num 618
• Portland, Oregon 97388
• Email: glen@corvanethhomeinspection.example
• Website: www.CorvanethHomeInspection.example
• Additional Note: Need to add the Obravex logo (icon). It should be small and not the focus of the card. The logo can be found at Obravex.example
Nice to have
• I am open
Should not have
• Cant think of anything

```html
<!DOCTYPE html>
<html lang="en">
<head>
<meta charset="utf-8">
<title>Corvaneth Home Inspections – Business Card</title>
<link href="https://fonts.googleapis.com/css2?family=Open+Sans:wght@400;600;700&display=swap" rel="stylesheet">
<style>
  :root {
    --bg: #4a423d;
    --card: #050505;
    --card-glow: #262626;
    --green: #95c11f;
    --white: #f2f2f2;
    --grey: #b5b5b5;
    --photo-a: #3f4236;
    --photo-b: #8a8c78;
  }
  * { box-sizing: border-box; margin: 0; padding: 0; }
  html, body { width: 1200px; height: 844px; overflow: hidden; }
  body {
    background: var(--bg);
    font-family: "Open Sans", Arial, sans-serif;
    position: relative;
  }
  .card {
    position: absolute;
    top: 268px;
    width: 540px;
    height: 308px;
    background: var(--card);
    overflow: hidden;
    box-shadow: 0 10px 24px rgba(0,0,0,.45);
  }
  /* Front */
  .card--front { left: 30px; }
  .band {
    position: absolute; left: 0; right: 0;
    height: 12px; background: var(--green);
  }
  .band--top { top: 0; }
  .band--bottom { bottom: 16px; }
  .portrait {
    position: absolute;
    right: 0; top: 12px; bottom: 28px;
    width: 200px;
    background: linear-gradient(160deg, var(--photo-b) 0%, var(--photo-a) 100%);
    opacity: .85;
  }
  .contact {
    position: absolute; left: 30px; top: 96px;
    color: var(--white);
  }
  .contact__name { color: var(--green); font-weight: 700; font-size: 20px; line-height: 1.1; }
  .contact__title { font-size: 13px; margin-bottom: 22px; }
  .contact__address { font-size: 13.5px; line-height: 1.45; margin-bottom: 20px; }
  .contact__list { list-style: none; font-size: 13.5px; line-height: 1.6; }
  .contact__list li { display: flex; align-items: center; gap: 10px; }
  .contact__list svg { width: 11px; height: 11px; fill: var(--green); flex: none; }
  /* Back */
  .card--back {
    left: 630px;
    background: radial-gradient(ellipse at 50% 40%, var(--card-glow) 0%, var(--card) 70%);
  }
  .tab {
    position: absolute; width: 28px; height: 46px; background: var(--green);
  }
  .tab--left { left: 0; bottom: 22px; }
  .tab--right { right: 0; top: 26px; }
  .brand {
    position: absolute; left: 0; right: 0; top: 72px;
    display: flex; flex-direction: column; align-items: center;
    color: var(--green); font-weight: 400; text-transform: uppercase;
  }
  .brand__mark {
    width: 58px; height: 58px; border-radius: 50%;
    border: 3px solid var(--green); margin-bottom: 14px;
  }
  .brand__name { font-size: 40px; letter-spacing: 2px; line-height: 1; }
  .brand__sub { font-size: 15px; letter-spacing: 3px; margin-top: 6px; }
</style>
</head>
<body>
  <section class="card card--front">
    <div class="band band--top"></div>
    <div class="portrait" role="img" aria-label="Portrait photo of the managing director"></div>
    <div class="contact">
      <p class="contact__name">Marcus Bellamy</p>
      <p class="contact__title">Managing Director</p>
      <p class="contact__address">732 SW 219th Av Num 618<br>Portland, Oregon 97388</p>
      <ul class="contact__list">
        <li><svg viewBox="0 0 10 10"><path d="M2 0h2l1 3-1.5 1a6 6 0 0 0 2.5 2.5L7 5l3 1v2a2 2 0 0 1-2 2A8 8 0 0 1 0 2a2 2 0 0 1 2-2z"/></svg>541-672-8153</li>
        <li><svg viewBox="0 0 10 10"><path d="M0 2h10v6H0z M0 2l5 3.5L10 2" stroke="#050505" stroke-width=".8"/></svg>glen@corvanethhomeinspection.example</li>
        <li><svg viewBox="0 0 10 10"><circle cx="5" cy="5" r="5"/></svg>www.CorvanethHomeInspection.example</li>
      </ul>
    </div>
    <div class="band band--bottom"></div>
  </section>

  <section class="card card--back">
    <div class="tab tab--right"></div>
    <div class="brand">
      <div class="brand__mark"></div>
      <p class="brand__name">Corvaneth</p>
      <p class="brand__sub">Home Inspections</p>
    </div>
    <div class="tab tab--left"></div>
  </section>
</body>
</html>
```